Brindlewave Microdevices Core Values Posters + Icons

Interested in helping us refresh our core values posters? Click on the attached document for more details! (review brindlewavemicro.com for more information about Brindlewave)

Deliverables are the following:
o 6 Core Value Posters – each shows the core value and the statement that accompanies that value (e.g. “Accountability” and “We keep our Promises.”) and smaller representations of the other 5 values (see concept sketch)
o 6 Core Value icons – an image that demonstrates the core value that can be placed large on each poster and repurposed on things like coasters and awards.
Updates

Project Deadline Extended
Reason: There are some great designs being submitted and they still need a bit more work. Have an idea? Submit yours now!

Target Market(s)

Employees of Brindlewave Microdevices Worldwide

Font styles to use
Sans Serif

Requirements
Must have
• Must have:
• Core Values and We Statements
• Icon Associated with each Core Value
• Clean design with strong emphasis on the featured core value/we statement pair
Nice to have
• Must make sense globally

```html
<!DOCTYPE html>
<html lang="en">
<head>
<meta charset="utf-8">
<title>Brindlewave Microdevices – Quality</title>
<link href="https://fonts.googleapis.com/css2?family=Roboto+Condensed:wght@700&display=swap" rel="stylesheet">
<style>
  :root {
    --paper: #ffffff;
    --glow: #5cb0dc;
    --mid-blue: #4877b4;
    --deep-indigo: #2b1f72;
    --mark-indigo: #271a6b;
    --white: #ffffff;
    --gold: #f7c21c;
    --ink: #0f0f2e;
  }
  * { margin: 0; padding: 0; box-sizing: border-box; }
  html, body { width: 960px; height: 1200px; overflow: hidden; background: var(--paper); }
  body { font-family: "Roboto Condensed", "Arial Narrow", sans-serif; position: relative; }

  .poster {
    position: absolute; left: 40px; top: 40px; width: 880px; height: 1120px;
    background: radial-gradient(ellipse 62% 52% at 50% 43%, var(--glow) 0%, var(--mid-blue) 55%, var(--deep-indigo) 100%);
    overflow: hidden;
  }

  .values-row { position: absolute; top: 38px; left: 0; width: 100%; height: 120px; }
  .value { position: absolute; width: 160px; margin-left: -80px; text-align: center; color: var(--white); }
  .value svg { display: block; margin: 0 auto; width: 80px; height: 72px; }
  .value-label { display: block; margin-top: 12px; font-size: 15px; letter-spacing: 0.2px; text-transform: uppercase; }

  .feature-icon {
    position: absolute; left: 324px; top: 290px; width: 232px; height: 426px;
    background: var(--mark-indigo); border-radius: 18px;
  }
  .feature-shadow {
    position: absolute; left: 320px; top: 736px; width: 240px; height: 16px;
    border-radius: 50%; background: radial-gradient(ellipse at center, rgba(39,26,107,0.85), rgba(39,26,107,0) 70%);
  }

  .value-title {
    position: absolute; top: 818px; left: 0; width: 100%; text-align: center;
    color: var(--white); font-size: 96px; line-height: 1; letter-spacing: 1px;
  }
  .value-statement {
    position: absolute; top: 928px; left: 0; width: 100%; text-align: center;
    color: var(--white); font-size: 56px; line-height: 1;
  }

  .brand {
    position: absolute; top: 982px; left: 0; width: 100%;
    display: flex; justify-content: center; align-items: center; gap: 12px;
  }
  .brand-square { width: 34px; height: 34px; background: var(--gold); }
  .brand-name { color: var(--ink); font-size: 36px; line-height: 1; }

  .mission {
    position: absolute; top: 1050px; left: 0; width: 100%; text-align: center;
    color: var(--gold); font-size: 30px; line-height: 1; letter-spacing: 0.3px;
  }
</style>
</head>
<body>
<main class="poster">
  <nav class="values-row" aria-label="Core values">
    <div class="value" style="left:166px">
      <svg viewBox="0 0 80 72" aria-hidden="true">
        <path d="M28 42 L18 68 L26 64 L30 71 L38 48 Z M52 42 L62 68 L54 64 L50 71 L42 48 Z" fill="#fff"/>
        <circle cx="40" cy="28" r="26" fill="#fff"/>
        <circle cx="40" cy="28" r="16" fill="none" stroke="#3b4f9a" stroke-width="3"/>
        <polygon points="40,17 43,25 51,25 45,30 47,38 40,33 33,38 35,30 29,25 37,25" fill="#3b4f9a"/>
      </svg>
      <span class="value-label">Customer Obsession</span>
    </div>
    <div class="value" style="left:338px">
      <svg viewBox="0 0 80 72" aria-hidden="true">
        <circle cx="38" cy="38" r="32" fill="#fff"/>
        <circle cx="38" cy="38" r="22" fill="#3f559e"/>
        <circle cx="38" cy="38" r="15" fill="#fff"/>
        <circle cx="38" cy="38" r="7" fill="#3f559e"/>
        <line x1="40" y1="36" x2="68" y2="10" stroke="#fff" stroke-width="3"/>
        <path d="M64 6 L72 6 L72 14 Z" fill="#fff"/>
      </svg>
      <span class="value-label">Accountability</span>
    </div>
    <div class="value" style="left:484px">
      <svg viewBox="0 0 80 72" aria-hidden="true">
        <circle cx="40" cy="22" r="11" fill="#fff"/>
        <circle cx="20" cy="30" r="7" fill="#fff"/>
        <circle cx="60" cy="30" r="7" fill="#fff"/>
        <path d="M24 56 Q24 36 40 36 Q56 36 56 56 Z" fill="#fff"/>
        <path d="M6 54 Q8 40 20 40 Q30 40 30 50 L28 54 Z M74 54 Q72 40 60 40 Q50 40 50 50 L52 54 Z" fill="#fff"/>
      </svg>
      <span class="value-label">Teamwork</span>
    </div>
    <div class="value" style="left:632px">
      <svg viewBox="0 0 80 72" aria-hidden="true">
        <path d="M4 40 Q24 34 34 30 L32 46 Q18 44 4 40 Z" fill="#fff"/>
        <circle cx="50" cy="42" r="24" fill="#fff"/>
        <circle cx="50" cy="42" r="18" fill="#4a6aae"/>
        <rect x="46" y="10" width="8" height="6" fill="#fff"/>
        <line x1="50" y1="42" x2="56" y2="28" stroke="#fff" stroke-width="3"/>
      </svg>
      <span class="value-label">Speed</span>
    </div>
    <div class="value" style="left:746px">
      <svg viewBox="0 0 80 72" aria-hidden="true">
        <g stroke="#d7dcef" stroke-width="3">
          <line x1="40" y1="26" x2="40" y2="2"/><line x1="40" y1="26" x2="62" y2="6"/>
          <line x1="40" y1="26" x2="18" y2="6"/><line x1="40" y1="26" x2="70" y2="26"/>
          <line x1="40" y1="26" x2="10" y2="26"/><line x1="40" y1="26" x2="66" y2="44"/>
          <line x1="40" y1="26" x2="14" y2="44"/>
        </g>
        <circle cx="40" cy="26" r="14" fill="#fff"/>
        <path d="M34 40 L46 40 L46 56 L52 56 L40 70 L28 56 L34 56 Z" fill="#fff"/>
      </svg>
      <span class="value-label">Innovation</span>
    </div>
  </nav>

  <div class="feature-icon" role="img" aria-label="Large quality core value icon"></div>
  <div class="feature-shadow" aria-hidden="true"></div>

  <h1 class="value-title">QUALITY</h1>
  <p class="value-statement">We deliver confidence.</p>

  <div class="brand">
    <span class="brand-square" aria-hidden="true"></span>
    <span class="brand-name">Brindlewave Microdevices</span>
  </div>

  <p class="mission">Accelerating customer innovation for a better connected world</p>
</main>
</body>
</html>
```